Conference program advertisement

Our business www.clinic ledgerwise.com.au is a good sponsor of the conference program run by the Pacific Rim Guild of Perioperative Medicine (PRGPM) here in Western Australia.
We have been running the same ad for a while and so we could do with a fresh new presence.
We have a conference banner and other signage that we'll use at the trade show so we're not looking to rebrand. Just looking for a new ad.
Specification is full colour A4, high res PDF
(Because I'm using my phone to create this job, I cannot seem to upload the existing ad. I'll do do ASAP.)

Target Market(s)

Specialist doctors

Industry/Entity Type

Trade

Font styles to use
Sans Serif

Colors

Designer to choose colors to be used in the design.

Requirements
Must have
• A4
Existing logo and colour scheme

```html
<!DOCTYPE html>
<html lang="en">
<head>
<meta charset="utf-8">
<title>Clinic Ledgerwise Services – Advertisement</title>
<link href="https://fonts.googleapis.com/css2?family=Barlow:wght@400;500;600&family=Roboto+Condensed:wght@700&display=swap" rel="stylesheet">
<style>
  :root {
    --red: #c8262f;
    --ink: #1a1a1a;
    --paper: #ffffff;
    --box-edge: #d4d4d4;
    --box-shade: #e9e9e9;
    --teal-dark: #0f5f63;
    --teal-mid: #2f9ea0;
    --teal-light: #9fe0df;
  }
  * { margin: 0; padding: 0; box-sizing: border-box; }
  html, body { width: 849px; height: 1200px; overflow: hidden; background: var(--paper); }
  .ad {
    position: relative; width: 849px; height: 1200px; overflow: hidden;
    font-family: "Barlow", Arial, sans-serif; color: var(--ink); background: var(--paper);
  }
  .hero {
    position: absolute; left: 0; top: 0; width: 849px; height: 552px;
    background:
      radial-gradient(ellipse at 55% 70%, var(--teal-light) 0%, rgba(159,224,223,0) 45%),
      linear-gradient(180deg, #b9c7c9 0%, var(--teal-mid) 40%, var(--teal-dark) 100%);
  }
  .headline {
    position: absolute; left: 0; top: 566px; width: 849px; text-align: center;
    font-family: "Roboto Condensed", "Arial Narrow", sans-serif; font-weight: 700;
    font-size: 64px; line-height: 67px; color: var(--red); letter-spacing: 0.8px;
  }
  .headline .dark { color: var(--ink); }
  .intro {
    position: absolute; left: 39px; top: 710px; width: 771px;
    font-size: 17.4px; line-height: 23.6px; font-weight: 500; text-align: justify;
    letter-spacing: 0.2px;
  }
  .service {
    position: absolute; display: flex; align-items: center; justify-content: center;
    text-align: center; font-size: 14.5px; line-height: 19px; letter-spacing: 0.4px;
    text-transform: uppercase; color: var(--ink);
    background: linear-gradient(180deg, var(--paper) 0%, var(--paper) 60%, var(--box-shade) 100%);
    border-left: 3px solid var(--box-edge); border-bottom: 2px solid var(--box-edge);
    box-shadow: 0 2px 3px rgba(0,0,0,0.08);
    padding: 0 10px;
  }
  .service.highlight { color: var(--red); }
  .col-a { left: 39px; width: 240px; }
  .col-b { left: 305px; width: 240px; }
  .col-c { left: 568px; width: 240px; }
  .contact {
    position: absolute; top: 1082px; font-size: 14px; line-height: 19px; color: var(--ink);
    font-style: normal;
  }
  .contact strong { font-weight: 600; }
  .contact.person { left: 39px; }
  .contact.postal { left: 341px; }
  .brand {
    position: absolute; left: 608px; top: 1076px; display: flex; align-items: center; gap: 12px;
  }
  .brand-square { width: 44px; height: 44px; background: var(--red); }
  .brand-name {
    font-family: "Barlow", Arial, sans-serif; font-weight: 500; font-size: 19px;
    line-height: 20px; color: var(--red); text-transform: uppercase;
  }
</style>
</head>
<body>
<main class="ad">
  <div class="hero" role="img" aria-label="Photograph of two surgeons in teal scrubs, caps and masks operating in a theatre"></div>

  <h1 class="headline">IS <span class="dark">ADMINISTRATION</span> EATING<br>UP YOUR VALUABLE TIME?</h1>

  <p class="intro">Admin can consume a large amount of time for doctors working in private practice. From generating accounts to chasing up bad debts, from sitting on hold with health funds, or trawling through remittance advices to getting accreditation papers and submitting provider number applications properly - we’re sure you would prefer to focus on being a doctor rather than worrying about paperwork and piles of admin. Clinic Ledgerwise Services is here to help - contact us today if you’re ready to remove the burden of admin.</p>

  <div class="service col-a" style="top:870px;height:30px;">Private Billing</div>
  <div class="service col-a highlight" style="top:911px;height:30px;">VMP Billing</div>
  <div class="service col-a" style="top:952px;height:30px;">Practice Management</div>
  <div class="service col-a highlight" style="top:992px;height:30px;">Organise Lists</div>
  <div class="service col-a" style="top:1032px;height:30px;">Cover Lists</div>

  <div class="service col-b highlight" style="top:870px;height:30px;">Banking</div>
  <div class="service col-b" style="top:911px;height:60px;">Carewell and Health<br>Fund Registrations</div>
  <div class="service col-b highlight" style="top:992px;height:70px;">Fee Estimates and Informed<br>Financial Consent</div>

  <div class="service col-c" style="top:870px;height:54px;">Paylink and Credit Card<br>Payments</div>
  <div class="service col-c highlight" style="top:933px;height:48px;">Electronic Claiming to<br>Health Funds</div>
  <div class="service col-c" style="top:992px;height:30px;">GST Reporting</div>
  <div class="service col-c highlight" style="top:1032px;height:30px;">Hospital Accreditations</div>

  <address class="contact person">
    <strong>Liam Hartwell</strong> Mobile +61 400 555 182<br>
    First Floor, Unit 12, 740 Harbour Street,<br>
    Eastmere, WA, 6099
  </address>
  <address class="contact postal">
    PO Box 318, Eastmere WA 6890<br>
    liam@clinicledgerwise.com.au<br>
    www.clinic ledgerwise.com.au
  </address>

  <div class="brand">
    <span class="brand-square"></span>
    <span class="brand-name">Clinic<br>Ledgerwise<br>Services</span>
  </div>
</main>
</body>
</html>
```